Website redesign for PR company

We currently have a Squarespace site, which has been sufficient during the start up stage of our public relations business. I would be interested to know whether there are options within the Squarespace functionality to dramatically improve the look of our site, or whether you recommend a full redesign using another web service.

I would like the designer to offer some suggestions for improvements to the current site and/or provide designs for a new site.

I would like for us to have an ongoing relationship keeping our site up to date. Our current site is at www.vorlo.co.nz

Target Market(s)

New Zealand primarily, government and commercial clients

Industry/Entity Type

public relations

Coding

Coded - Design and coding required

Number of Pages Required

5+ page

Requirements
Must have
• Vorlo Blue: R38 G34 B98 / #262261 / C100 M100 Y25 K25 Vorlo Orange: R247 G148 B29 / #f7931d / C0 M50 Y100 K0 Pink: R249 G181 B178 / #f8b4b2 / C0 M25 Y25 K0No stock imagery, use of our profile photos as on current site and custom graphics only.
Should not have
• stock images

```html
<!DOCTYPE html>
<html lang="en">
<head>
<meta charset="utf-8">
<title>Vorlo Communications</title>
<link href="https://fonts.googleapis.com/css2?family=Playfair+Display:wght@400;700&family=Mulish:wght@400;600;700&display=swap" rel="stylesheet">
<style>
:root{
  --blue:#262261;
  --navy:#1f1a5a;
  --orange:#f7931d;
  --pink:#f8b4b2;
  --lavender:#e9e7f5;
  --mist:#f3f2f6;
  --ink:#2b2b3a;
  --grey:#8f8ea0;
  --line:#b9b6d3;
  --white:#fff;
}
*{box-sizing:border-box;margin:0;padding:0}
html,body{width:1200px;height:4418px;overflow:hidden}
body{position:relative;background:var(--white);font-family:"Mulish",sans-serif;color:var(--ink)}
.abs{position:absolute}
.serif{font-family:"Playfair Display",serif}
.btn{display:inline-block;background:var(--orange);color:var(--white);font-family:"Mulish",sans-serif;font-weight:700;text-transform:uppercase;letter-spacing:.5px}

/* header */
.site-header{position:absolute;top:0;left:0;width:1200px;height:103px;background:var(--white);z-index:3}
.brand{position:absolute;left:132px;top:30px;font-family:"Playfair Display",serif;font-weight:700;font-size:40px;color:var(--blue);display:flex;align-items:baseline;gap:4px}
.brand-dot{width:8px;height:8px;border-radius:50%;background:var(--orange);display:inline-block}
.top-contacts{position:absolute;right:132px;top:16px;display:flex;align-items:center;font-size:12px;color:var(--ink)}
.top-contacts .sep{width:2px;height:22px;background:var(--blue);margin:0 12px}
.top-contacts .btn{margin-left:12px;padding:6px 12px;font-size:12px;text-transform:none;font-weight:600;letter-spacing:0}
.main-nav{position:absolute;right:132px;top:58px;display:flex;gap:31px;font-size:12px}
.main-nav a{color:var(--ink);text-decoration:none}
.main-nav a.active{color:var(--orange)}

/* hero */
.hero-image{position:absolute;top:0;left:0;width:1200px;height:682px;background:linear-gradient(160deg,#f4f4f4 0%,#d7d7d7 40%,#eeeeee 65%,#bdbdbd 100%)}
.hero-title{position:absolute;top:130px;left:0;width:1200px;text-align:center;font-family:"Playfair Display",serif}
.hero-title .l1{font-size:50px;color:var(--blue);font-weight:400;font-family:"Mulish",sans-serif}
.hero-title .l2{font-size:50px;color:var(--orange);font-weight:700;margin-top:4px}
.hero-title .rule{width:276px;height:2px;background:var(--orange);margin:10px auto 0}
.corner{position:absolute;width:10px;height:14px;background:var(--orange);top:682px}

/* about */
.about-frame{position:absolute;left:129px;top:734px;width:582px;height:456px;border:2px solid var(--blue)}
.about-accent{position:absolute;left:126px;top:826px;width:6px;height:248px;background:var(--orange)}
.about-text{position:absolute;left:183px;top:818px;width:300px;font-family:"Playfair Display",serif;font-size:17px;line-height:26px;color:var(--ink)}
.about-btn{position:absolute;left:185px;top:1029px;width:120px;height:37px;line-height:37px;text-align:center;font-size:12px}
.about-shadow{position:absolute;left:530px;top:770px;width:536px;height:368px;background:#8d8aa8}
.profile-photo{position:absolute;left:530px;top:782px;width:536px;height:356px;background:linear-gradient(90deg,#6b5a2b 0%,#8a7a45 30%,#b4232b 60%,#8c6d3c 100%)}
.texture{position:absolute;background:#f1f0f6}

/* services */
.services{position:absolute;left:0;top:1543px;width:1200px;height:640px;background:var(--lavender)}
.cell{position:absolute;text-align:center;color:var(--blue)}
.cell h3{font-family:"Playfair Display",serif;font-weight:700;font-size:18px;line-height:27px;color:var(--blue)}
.cell.feature h3{color:var(--orange);font-size:16px}
.cell p{font-size:11px;line-height:15px;margin-top:10px}
.cell .btn{margin-top:10px;padding:6px 10px;font-size:10px}
.vline{position:absolute;width:1px;background:var(--line)}
.hline{position:absolute;height:1px;background:var(--line)}
.bubble{position:absolute;border-radius:50%;background:#d3d0e8}

/* news */
.section-title{position:absolute;left:0;width:1200px;text-align:center;font-family:"Playfair Display",serif;font-weight:700;font-size:25px;color:var(--blue)}
.section-rule{position:absolute;left:574px;width:52px;height:2px;background:var(--orange)}
.news-card{position:absolute;top:2319px;width:298px;height:300px;background:var(--white);box-shadow:0 4px 18px rgba(38,34,97,.08);padding:34px 30px 0}
.news-card.active{border:2px solid var(--orange)}
.news-meta{font-size:11px;color:var(--ink)}
.news-card h4{font-family:"Playfair Display",serif;font-size:17px;line-height:23px;color:var(--ink);font-weight:400;margin-top:12px}
.news-card p{font-size:10px;line-height:14px;margin-top:20px}
.news-card .btn{position:absolute;left:30px;top:221px;padding:7px 10px;font-size:9.5px}
.news-card .band{position:absolute;left:0;bottom:0;width:100%;height:18px;background:#f1f0f6}

/* testimonials */
.quote-section{position:absolute;left:0;top:2683px;width:1200px;height:460px;background:var(--mist)}
.quote-text{position:absolute;left:300px;top:2894px;width:600px;text-align:center;font-size:16px;line-height:26px;color:var(--ink)}
.quote-mark{position:absolute;font-family:"Playfair Display",serif;font-weight:700;font-size:44px;color:var(--orange);line-height:1}
.quote-name{position:absolute;left:0;top:3030px;width:1200px;text-align:center;font-size:16px}
.quote-role{position:absolute;left:0;top:3056px;width:1200px;text-align:center;font-size:11px}

/* events */
.event-image{position:absolute;left:132px;top:3326px;width:557px;height:428px;background:linear-gradient(160deg,#c48a4d 0%,#f5d39a 35%,#f0b463 65%,#b2773f 100%)}
.event-box{position:absolute;left:646px;top:3378px;width:420px;height:342px;background:var(--navy);color:var(--white);padding:66px 60px 0}
.event-box h3{font-family:"Playfair Display",serif;font-weight:700;font-size:25px}
.event-box p{font-size:11px;line-height:15px;margin-top:16px;color:#e4e2f1}
.event-box .btn{margin-top:30px;padding:11px 21px;font-size:12px}

/* organisations */
.orgs{position:absolute;left:0;top:3819px;width:1200px;height:300px;background:var(--mist)}
.org-tile{position:absolute;top:3953px;width:182px;height:76px;background:var(--white);display:flex;align-items:center;justify-content:center;gap:7px;font-family:"Mulish",sans-serif;font-weight:600;font-size:14px;color:var(--blue)}
.org-tile .mark{width:14px;height:14px;background:#8e8bb2;border-radius:50%}
.pager{position:absolute;top:4069px;width:6px;height:6px;border-radius:50%;background:#c7c6d2}

/* footer */
.footer-brand{position:absolute;left:126px;top:4180px;font-family:"Playfair Display",serif;font-weight:700;font-size:46px;color:var(--white);display:flex;align-items:baseline;gap:5px}
.footer-brand .brand-dot{background:var(--white)}
.footer-divider{position:absolute;left:254px;top:4177px;width:1px;height:86px;background:var(--orange)}
.footer-info{position:absolute;font-size:11px;line-height:16px;color:var(--white)}
.footer-links{position:absolute;left:135px;top:4292px;width:930px;display:flex;justify-content:space-between;font-size:12px;color:var(--white)}
.footer-rule{position:absolute;left:132px;top:4338px;width:934px;height:1px;background:#4a4684}
.copyright{position:absolute;left:132px;top:4365px;font-size:12px;color:var(--white)}
.follow{position:absolute;left:940px;top:4235px;font-size:12px;color:var(--white);display:flex;align-items:center;gap:10px}
.social{display:flex;align-items:center;gap:6px;font-weight:700;font-size:12px;color:var(--white)}
.social-dot{width:10px;height:10px;border-radius:50%;background:var(--white)}
</style>
</head>
<body>

<!-- hero -->
<div class="hero-image" role="img" aria-label="Black and white upward view of glass office towers"></div>
<div class="corner" style="left:0"></div>
<div class="corner" style="left:1190px"></div>

<header class="site-header">
  <div class="brand">vorlo<span class="brand-dot"></span></div>
  <div class="top-contacts">
    <span>Jess 021 555 0148</span><span class="sep"></span><span>Mara 022 555 0193</span>
    <span class="btn">Contact Us</span>
  </div>
  <nav class="main-nav">
    <a class="active">Who we are</a><a>How we can help</a><a>Where we come from</a><a>Working with Vorlo</a><a>Vorlo community</a><a>Newsfeed</a><a>Events</a>
  </nav>
</header>

<div class="hero-title">
  <div class="l1">People with</div>
  <div class="l2">Energy|</div>
  <div class="rule"></div>
</div>

<!-- about -->
<div class="about-frame"></div>
<div class="about-accent"></div>
<p class="about-text">Mara Collins-Reid and Jess<br>Whitcombe have worked in and<br>around communications and politics<br>for over a decade. They will ensure<br>your voice and story is heard by the<br>right people to have maximum<br>impact.</p>
<span class="btn about-btn">Read More</span>
<div class="about-shadow"></div>
<div class="profile-photo" role="img" aria-label="Portrait photo of the two founders"></div>
<div class="texture" style="left:1070px;top:1040px;width:32px;height:90px" role="img" aria-label="Light dot texture"></div>
<div class="texture" style="left:940px;top:1140px;width:162px;height:34px" role="img" aria-label="Light dot texture"></div>

<!-- services backdrop -->
<div class="services"></div>

<!-- blue statement band -->
<svg class="abs" style="left:0;top:1222px" width="1200" height="366" viewBox="0 0 1200 366">
  <polygon points="0,0 1200,78 1200,100 0,14" fill="var(--orange)"/>
  <polygon points="0,14 1200,76 1200,356 0,262" fill="var(--navy)"/>
  <polygon points="0,262 1200,332 1200,356 0,284" fill="var(--orange)"/>
</svg>
<p class="abs serif" style="left:150px;top:1359px;width:900px;text-align:center;color:#fff;font-size:17px;line-height:32px">Great PR is built on excellent communication and strong relationships. That's what we do.<br>We offer strategic advice and hands-on advocacy support to ensure you are heard and<br>understood by the public, media and stakeholders.</p>

<div class="bubble" style="left:-30px;top:1573px;width:74px;height:74px"></div>
<div class="bubble" style="left:1172px;top:1693px;width:50px;height:50px"></div>
<div class="bubble" style="left:-20px;top:2140px;width:45px;height:45px"></div>
<div class="bubble" style="left:1166px;top:2100px;width:90px;height:90px"></div>

<!-- service grid -->
<div class="vline" style="left:442px;top:1617px;height:529px"></div>
<div class="vline" style="left:759px;top:1617px;height:529px"></div>
<div class="hline" style="left:129px;top:1860px;width:939px"></div>

<div class="cell" style="left:129px;top:1710px;width:313px">
  <svg width="58" height="54" viewBox="0 0 58 54" fill="none" stroke="var(--blue)" stroke-width="2"><path d="M8 50 L40 8 a5 5 0 0 1 8 6 L16 52 Z M12 46 l4 4 M34 14 l8 6"/></svg>
  <h3 style="font-size:24px;margin-top:6px">How we can help</h3>
</div>
<div class="cell feature" style="left:442px;top:1630px;width:317px">
  <svg width="56" height="74" viewBox="0 0 56 74" fill="none" stroke="var(--orange)" stroke-width="2"><circle cx="28" cy="14" r="4"/><path d="M18 6a13 13 0 0 0 0 16M38 6a13 13 0 0 1 0 16M12 2a20 20 0 0 0 0 24M44 2a20 20 0 0 1 0 24M28 18 L10 72 M28 18 L46 72 M18 46h20 M14 60h28 M20 40l20 20 M36 40L16 60"/></svg>
  <h3 style="margin-top:6px">Be understood</h3>
  <p>Take up every opportunity: Use Vorlo<br>for opinion and feature writing</p>
  <span class="btn">Read More</span>
</div>
<div class="cell" style="left:759px;top:1698px;width:309px">
  <svg width="76" height="58" viewBox="0 0 76 58" fill="none" stroke="var(--blue)" stroke-width="2"><path d="M8 20h14l26-14v44L22 36H8z M14 36l6 18h8l-4-18 M56 28h10 M56 14l8-6 M56 42l8 6"/></svg>
  <h3 style="margin-top:8px">Be heard</h3>
</div>
<div class="cell" style="left:129px;top:1930px;width:313px">
  <svg width="76" height="76" viewBox="0 0 76 76" fill="none" stroke="var(--blue)" stroke-width="2"><circle cx="38" cy="38" r="34"/><circle cx="38" cy="38" r="4"/><path d="M52 22 L42 42 22 54 34 34Z M38 4v6 M38 66v6 M4 38h6 M66 38h6"/></svg>
  <h3 style="margin-top:18px">Navigate the<br>political arena</h3>
</div>
<div class="cell" style="left:442px;top:1930px;width:317px">
  <svg width="76" height="76" viewBox="0 0 76 76" fill="none" stroke="var(--blue)" stroke-width="2"><path d="M70 6 C52 6 38 16 28 34 L42 48 C60 38 70 24 70 6Z M28 34 L14 36 6 50 22 48 M42 48 L40 62 26 70 28 54 M22 54 L10 66 M18 50l-8 6 M26 58l-6 8"/><circle cx="52" cy="24" r="5"/></svg>
  <h3 style="margin-top:18px">Make simple<br>improvements, fast</h3>
</div>
<div class="cell" style="left:759px;top:1930px;width:309px">
  <svg width="76" height="76" viewBox="0 0 76 76" fill="none" stroke="var(--blue)" stroke-width="2"><path d="M6 14 L14 6 70 62 62 70Z M20 20l6-6 M30 30l6-6 M40 40l6-6 M50 50l6-6 M60 6 L70 16 22 64 10 70 14 56Z M14 56l8 8"/></svg>
  <h3 style="margin-top:18px">Measure<br>performance</h3>
</div>

<!-- latest news -->
<h2 class="section-title" style="top:2226px">Latest News</h2>
<div class="section-rule" style="top:2277px"></div>

<article class="news-card" style="left:129px">
  <div class="news-meta">May 2, 2022 | &nbsp; Jess Whitcombe</div>
  <h4>Have you heard the news? The press release is (mostly) dead.</h4>
  <p>It was once believed that a concise, formally-toned paragraph was the key to a successful media outreach. But these days there are better ways to go about marketing your cause.</p>
  <span class="btn">Read More</span><div class="band"></div>
</article>
<article class="news-card active" style="left:447px">
  <div class="news-meta">May 2, 2022 | &nbsp; Jess Whitcombe</div>
  <h4>Get the most out of your<br>comms in 2022</h4>
  <p>In 2022, the impact of the pandemic continues to touch every aspect of life and business in Aotearoa. With the right angle directed at the right news outlet, your story has a chance of getting cut-through.</p>
  <span class="btn">Read More</span><div class="band"></div>
</article>
<article class="news-card" style="left:768px">
  <div class="news-meta">May 27, 2022 | &nbsp; Mara Collins-Reid</div>
  <h4>Tips from the<br>Newsroom</h4>
  <p>Tips from the newsroom - our June media workshop will be hosted by former Dayline and Harbour Times reporter Lena Hart and will focus on how to get your stories heard in today's media environment.</p>
  <span class="btn">Read More</span><div class="band"></div>
</article>

<!-- testimonials -->
<div class="quote-section"></div>
<svg class="abs" style="left:0;top:2680px" width="1200" height="60" viewBox="0 0 1200 60">
  <polygon points="0,0 1200,0 1200,40 0,0" fill="var(--white)"/>
  <polygon points="420,0 1200,40 1200,58 600,22" fill="var(--orange)"/>
</svg>
<h2 class="section-title" style="top:2790px">What our Clients say</h2>
<div class="section-rule" style="top:2841px"></div>
<span class="quote-mark" style="left:270px;top:2870px">&ldquo;</span>
<p class="quote-text">Simply put, Vorlo support the Kin Collective team with a wide range of critical expertise to ensure that our communications are contemporary, relevant and fit for purpose. I have found the team at Vorlo to be very professional, forward thinking and totally in line with the ethos and brand of Kin Collective.</p>
<span class="quote-mark" style="left:864px;top:2980px">&rdquo;</span>
<p class="quote-name">Tom Ashdown</p>
<p class="quote-role">Stakeholder Director, Kin Collective New Zealand</p>
<svg class="abs" style="left:128px;top:2922px" width="32" height="14" viewBox="0 0 32 14" fill="none" stroke="var(--ink)" stroke-width="1.5"><path d="M30 7H2M8 1L2 7l6 6"/></svg>
<svg class="abs" style="left:1038px;top:2922px" width="32" height="14" viewBox="0 0 32 14" fill="none" stroke="var(--ink)" stroke-width="1.5"><path d="M2 7h28M24 1l6 6-6 6"/></svg>
<svg class="abs" style="left:0;top:3100px" width="1200" height="110" viewBox="0 0 1200 110">
  <polygon points="0,0 1200,104 1200,110 0,110" fill="var(--white)"/>
  <polygon points="0,0 0,22 1200,110 1200,96" fill="var(--orange)"/>
</svg>

<!-- events -->
<h2 class="section-title" style="top:3223px">Upcoming Events</h2>
<div class="section-rule" style="top:3274px"></div>
<div class="event-image" role="img" aria-label="Illustration of a person working at a laptop at a desk by a window"></div>
<div class="event-box">
  <h3>BIM writing 101</h3>
  <p>Election season starts early in politics, and before you know it, it's BIM time again. With new Ministers on the horizon now is the time to consider your key messages to decisionmakers. Join our BIM101 ahead of drafting your Briefing to Incoming Ministers.</p>
  <span class="btn">Register</span>
</div>

<!-- organisations -->
<div class="orgs"></div>
<h2 class="section-title" style="top:3860px">Organisations With Vorlo</h2>
<div class="org-tile" style="left:129px"><span class="mark"></span>Kin Collective</div>
<div class="org-tile" style="left:321px"><span class="mark"></span>Review Panel</div>
<div class="org-tile" style="left:509px"><span class="mark"></span>Hui Tahi</div>
<div class="org-tile" style="left:697px"><span class="mark"></span>Transit Office</div>
<div class="org-tile" style="left:885px"><span class="mark"></span>Justice Office</div>
<svg class="abs" style="left:88px;top:3984px" width="12" height="16" viewBox="0 0 12 16" fill="none" stroke="var(--ink)" stroke-width="1.5"><path d="M9 2L3 8l6 6"/></svg>
<svg class="abs" style="left:1100px;top:3984px" width="12" height="16" viewBox="0 0 12 16" fill="none" stroke="var(--ink)" stroke-width="1.5"><path d="M3 2l6 6-6 6"/></svg>
<span class="pager" style="left:568px"></span><span class="pager" style="left:582px"></span><span class="pager" style="left:596px;background:var(--orange)"></span><span class="pager" style="left:610px"></span><span class="pager" style="left:624px"></span>

<!-- footer -->
<svg class="abs" style="left:0;top:4097px" width="1200" height="321" viewBox="0 0 1200 321">
  <polygon points="0,0 1200,62 1200,321 0,321" fill="var(--navy)"/>
  <polygon points="0,0 1200,50 1200,64 0,8" fill="var(--orange)"/>
</svg>
<div class="footer-brand">vorlo<span class="brand-dot"></span></div>
<div class="footer-divider"></div>
<svg class="abs" style="left:287px;top:4182px" width="10" height="13" viewBox="0 0 10 13" fill="#fff"><path d="M5 0a5 5 0 0 0-5 5c0 4 5 8 5 8s5-4 5-8a5 5 0 0 0-5-5zm0 7a2 2 0 1 1 0-4 2 2 0 0 1 0 4z"/></svg>
<div class="footer-info" style="left:285px;top:4208px">Kauri House<br>Level 2, 14 Tory St<br>Wellington 6011</div>
<svg class="abs" style="left:434px;top:4184px" width="13" height="10" viewBox="0 0 13 10" fill="#fff"><path d="M0 0h13v10H0z"/><path d="M0 0l6.5 5L13 0" stroke="#1f1a5a" fill="none"/></svg>
<div class="footer-info" style="left:432px;top:4208px">Email us<br>hello@vorlo.co.nz</div>
<div class="follow">Follow us <span class="social"><span class="social-dot"></span>Netlink</span></div>
<nav class="footer-links"><span>Who we are</span><span>How we can help</span><span>Where we come from</span><span>Working with Vorlo</span><span>Vorlo community</span><span>Newsfeed</span><span>Events</span></nav>
<div class="footer-rule"></div>
<p class="copyright">© 2022 Vorlo Communications Limited</p>

</body>
</html>
```